Furrow Glen Animal Hospital Postcard Design

I need a postcard for grand opening. The front of the card should have our business name and logo, below the logo I want to have a coupon for " Free office visit or $ 20 off of packages " for the first time clients.

I want to have the packages prices and details on the back of the postcard, the details of the packages are attached.

```html
<!DOCTYPE html>
<html lang="en">
<head>
<meta charset="utf-8">
<title>Furrow Glen Animal Hospital – Grand Opening Postcard</title>
<link href="https://fonts.googleapis.com/css2?family=Montserrat:wght@600;700&family=PT+Sans:wght@700&family=Lato:wght@400;700&display=swap" rel="stylesheet">
<style>
  :root {
    --backdrop: #767676;
    --navy: #0d2140;
    --blue: #1e88f0;
    --charcoal: #2d2d2d;
    --panel: #eeeeee;
    --white: #ffffff;
    --ink: #1c1c1c;
  }
  * { margin: 0; padding: 0; box-sizing: border-box; }
  html, body { width: 1200px; height: 1200px; overflow: hidden; }
  body { background: var(--backdrop); position: relative; font-family: "Lato", sans-serif; }

  .postcard {
    position: absolute; left: 110px; width: 944px; height: 472px;
    background: var(--white); overflow: hidden;
    box-shadow: 6px 6px 10px rgba(0,0,0,.45);
  }
  .postcard--front { top: 98px; }
  .postcard--back { top: 634px; }
  .postcard > * { position: absolute; }
  .bands { left: 0; top: 0; }

  .photo { border-radius: 2px; }
  .photo--round { border-radius: 50%; border: 6px solid var(--blue); box-shadow: 0 0 0 3px var(--white); }

  .text-panel { left: 139px; top: 0; width: 373px; height: 247px; background: linear-gradient(180deg, #f4f4f4, var(--panel)); }
  .logo-text { font-family: "Montserrat", sans-serif; font-weight: 600; letter-spacing: 1px; }
  .front-logo { left: 139px; width: 373px; top: 26px; text-align: center; font-size: 29px; color: var(--blue); }
  .business-name { left: 139px; width: 373px; top: 88px; text-align: center; font-family: "PT Sans", sans-serif; font-weight: 700; font-size: 45px; color: var(--blue); }
  .intro { left: 155px; top: 143px; width: 343px; font-size: 10.6px; line-height: 13px; color: var(--ink); text-align: justify; }

  .coupon {
    left: 69px; top: 315px; width: 201px; height: 92px;
    background: var(--white); border: 2px dashed var(--blue); border-radius: 5px;
    outline: 2px solid var(--white); text-align: center;
  }
  .coupon__lead { margin-top: 2px; font-size: 20px; color: var(--ink); }
  .coupon__amount { font-family: "Montserrat", sans-serif; font-weight: 700; font-size: 35px; line-height: 38px; color: var(--blue); }
  .coupon__note { font-size: 11.5px; color: var(--ink); white-space: nowrap; }

  .package h3 { font-size: 13px; font-weight: 700; margin-bottom: 4px; white-space: nowrap; }
  .package ul { list-style: none; }
  .package li { position: relative; padding-left: 13px; font-size: 9.6px; line-height: 14.2px; white-space: nowrap; }
  .package li::before {
    content: ""; position: absolute; left: 2px; top: 4px; width: 3px; height: 6px;
    border: solid var(--blue); border-width: 0 1.6px 1.6px 0; transform: rotate(40deg);
  }
  .package--dark h3 { color: var(--white); font-weight: 400; }
  .package--dark li { color: #e4e9f2; }
  .package--light h3 { color: var(--blue); font-weight: 400; }
  .package--light li { color: var(--ink); font-size: 11px; line-height: 16.4px; padding-left: 14px; }
  .package--light li::before { top: 4px; }
  .package--light h3.small { font-size: 11px; }

  .contact-pill {
    left: 678px; top: 387px; width: 280px; height: 25px; border-radius: 13px 0 0 13px;
    background: var(--blue); color: var(--white); font-size: 15px; line-height: 25px; padding-left: 10px;
  }
  .contact-line { left: 0; width: 944px; top: 398px; text-align: center; color: var(--blue); font-size: 15px; }

  .footer-bar { left: 0; bottom: 0; width: 944px; height: 48px; background: var(--charcoal); color: var(--white); text-align: center; line-height: 48px; font-size: 16px; letter-spacing: 3.5px; }
  .postcard--front .footer-bar { height: 49px; }

  .back-logo { left: 42px; top: 52px; font-size: 30px; color: var(--white); }
</style>
</head>
<body>

<section class="postcard postcard--front">
  <svg class="bands" width="944" height="472" viewBox="0 0 944 472">
    <path d="M0,238 Q520,300 944,62 V423 H0 Z" fill="var(--charcoal)"/>
    <path d="M0,262 Q520,310 944,70 V423 H0 Z" fill="var(--blue)"/>
    <path d="M0,296 Q540,318 944,95 V423 H0 Z" fill="var(--navy)"/>
  </svg>
  <div class="text-panel"></div>
  <div class="photo" role="img" aria-label="Tabby cat peeking from behind the panel" style="left:70px;top:66px;width:69px;height:181px;background:linear-gradient(160deg,#8a7a66,#d8d0c4 60%,#f3f1ee);"></div>
  <div class="photo" role="img" aria-label="Brown dog leaning in from the side" style="left:512px;top:3px;width:120px;height:215px;background:linear-gradient(160deg,#c98a4a,#a8652e 55%,#e9c9a2);"></div>
  <div class="photo photo--round" role="img" aria-label="Long-haired tabby cat lying down" style="left:720px;top:34px;width:188px;height:188px;background:radial-gradient(circle,#8c7a63,#5a4a3a 70%,#c9b9a2);"></div>

  <div class="logo-text front-logo">COMPANY LOGO</div>
  <div class="business-name">Business name</div>
  <p class="intro">Lorem Ipsum is simply dummy text of the printing and typesetting industry. Lorem Ipsum has been the industry's standard dummy text ever since the 1500s, when an unknown printer took a galley of type and scrambled it to make a type specimen book. It has survived not only five centuries, but also the leap into electronic typesetting, remaining essentially unchanged.</p>

  <div class="coupon">
    <div class="coupon__lead">Free office visit or</div>
    <div class="coupon__amount">$ 20 OFF</div>
    <div class="coupon__note">of packages for the first time clients</div>
  </div>

  <div class="package package--dark" style="left:474px;top:278px;">
    <h3>Annual dog package&nbsp; $99.</h3>
    <ul>
      <li>compete physical exam</li><li>DHLPP Vaccine</li><li>Bordetella vaccine</li>
      <li>Rabies vaccine</li><li>Fecal exam</li><li>Hecrtworm text</li><li>Deworming</li>
    </ul>
  </div>
  <div class="package package--dark" style="left:688px;top:278px;">
    <h3>Puppy package 1 [7-10 weekly]&nbsp; $49</h3>
    <ul>
      <li>Compete physical exam</li><li>DHPP vaccine</li><li>Bordetella vaccine</li>
      <li>Fecal exam</li><li>Deworming</li>
    </ul>
  </div>
  <div class="contact-pill">CONTUCT US : 123-456-789</div>
  <div class="footer-bar">www.furrowglenvet.com</div>
</section>

<section class="postcard postcard--back">
  <svg class="bands" width="944" height="472" viewBox="0 0 944 472">
    <path d="M0,0 H944 V90 Q470,40 0,240 Z" fill="var(--charcoal)"/>
    <path d="M0,0 H944 V84 Q470,30 0,232 Z" fill="var(--blue)"/>
    <path d="M0,0 H944 V54 Q470,20 0,222 Z" fill="var(--navy)"/>
  </svg>
  <div class="logo-text back-logo">COMPANY LOGO</div>
  <div class="photo photo--round" role="img" aria-label="Grey and white cat resting" style="left:744px;top:8px;width:188px;height:188px;background:radial-gradient(circle,#c9c4bd,#9f978d 60%,#efece8);"></div>
  <div class="photo" role="img" aria-label="Golden retriever lying down" style="left:646px;top:202px;width:276px;height:220px;background:radial-gradient(ellipse at 60% 45%,#d89a5a,#e8c08f 55%,rgba(255,255,255,0) 75%);"></div>

  <div class="package package--light" style="left:41px;top:233px;">
    <h3>Puppy package -2 [10-13 weekly]&nbsp; $49</h3>
    <ul><li>Compete physical exam</li><li>DHPP vaccine</li><li>Bordetella vaccine</li><li>Fecal exam</li><li>Deworming</li></ul>
    <h3 style="margin-top:6px;">kitten pakage 1[7-10 weekly]&nbsp; $49</h3>
    <ul><li>Compete physical exam</li><li>FVRCP Vaccine</li><li>Rabies vaccine</li><li>Deworming</li></ul>
  </div>
  <div class="package package--light" style="left:288px;top:181px;">
    <h3>Puppy package -3[13-14 weekly] $49</h3>
    <ul><li>Compete physical exam</li><li>DHPP vaccine</li><li>Rabies vaccine</li><li>Fecal exam</li><li>Deworming</li></ul>
    <h3 style="margin-top:6px;">Annual cat package&nbsp; $49</h3>
    <ul><li>compete physical exam</li><li>FVRCP Vaccine</li><li>Rabies vaccine</li><li>Fecal exam</li><li>Deworming</li></ul>
  </div>
  <div class="package package--light" style="left:533px;top:181px;">
    <h3>Kitten pakage 3[10-13 weekly]&nbsp; $49</h3>
    <ul><li>Compete physical exam</li><li>FVRCP Vaccine</li><li>Rabies vaccine</li><li>Fecal exam</li><li>Deworming</li></ul>
    <h3 class="small" style="margin-top:8px;">Kitten pakage 2[10-13 weekly]&nbsp; $49</h3>
    <ul><li>Compete physical exam</li><li>FVRCP Vaccine</li><li>Fecal exam</li><li>Deworming</li></ul>
  </div>
  <div class="contact-line">CONTACT US : 123-456-789</div>
  <div class="footer-bar">www.furrowglenvet.com</div>
</section>

</body>
</html>
```